I have a PHP web application to manage IT support calls and require a front-end design and user logon screen.

I have attached the current design which needs improving.

I have 2 current designs. The 2nd design is one I have been working on but requires a "professional touch". I also require the tables designed with dummy data from the 1st design.

I have attached my company logo in AI format which I would like incorporated into the design. There should also be a placeholder to supply the users company name upon login.

The screenshots I have attached should explain what I am looking for.

The Home Page should include charts which show statistical information such as:
Number of support tickets logged per month. Bar Chart etc.
Number of currently open support tickets.
Number of Quote Requests awaiting a response.
Number of Files and file repository.
Number of Reports.
Number of Customers.

For the Jobs and Customers pages the table fields should be designed as per the attached screenshots but a better looking tables. The table options such as uploading a file and adding a customer - these options can be changed and displayed differently.

Quotes page should display quotes returned and a "request a quote form".

Files page should have a good structure for browsing through an archive of files.

Profile page should have the option to include a profile picture.

An additional side page should be created for a web based calendar (these calendar entries will be updated by code).

The navbar should also include an alerts section.
The current attached design I have is based on bootstraps navbar.

Inspiration: http://plenvaro.com/freebie/free-admin-templates-for-backend-panels/

Hopefully this above link will show you some navigation style designs that I am looking for.

Please note, I will be doing the PHP coding myself and it is just the page designs I require in either HTML and or PHP format. I also require the CSS files for this project.
I need the code in a format where I can add and remove items in the menu from the code and not PSD/image based format.

If you think this project requires a higher budget let me know what you would expect and I will increase it!

Any questions, please let me know.
Dummy data can be shown for design purposes.

I have provided you a dummy login to our current system to show you the system:
https://reef.vomilbrixtonsolutions.co.uk/
username: dan.hollow@vomilbrixtonsolutions.co.uk
password:K#72zqTm

```html
<!DOCTYPE html>
<html lang="en">
<head>
<meta charset="utf-8">
<title>Vomil Brixton Solutions – Call out and support tracker</title>
<link href="https://fonts.googleapis.com/css2?family=Roboto:wght@400;500;700&display=swap" rel="stylesheet">
<style>
:root{
  --brand:#1f4a9e;
  --brand-dark:#173d86;
  --ring-grey:#a9a9a9;
  --text:#3c3c3c;
  --muted:#555;
  --rule:#d2d2d2;
  --side-bg:#eeeeee;
  --footer:#232323;
  --white:#fff;
}
*{box-sizing:border-box;margin:0;padding:0}
html,body{width:1200px;height:658px;overflow:hidden}
body{font-family:'Roboto',Arial,sans-serif;color:var(--text);position:relative;background:#e4e6e9}
.backdrop{position:absolute;left:0;top:86px;width:1200px;height:528px;
  background:radial-gradient(ellipse at 60% 30%,#f6f7f8 0%,#dfe2e5 55%,#c9ccd0 100%)}
.topbar{position:absolute;left:0;top:0;width:1200px;height:86px;background:var(--brand)}
.brand{position:absolute;left:174px;top:10px;height:66px;display:flex;align-items:center;gap:10px}
.brand-dot{width:30px;height:30px;border-radius:50%;border:3px solid var(--white)}
.brand-name{color:var(--white);font-weight:500;font-size:17px;line-height:1.1;width:110px}
.brand-divider{position:absolute;left:336px;top:10px;width:1px;height:66px;background:rgba(255,255,255,.8)}
.app-title{position:absolute;left:351px;top:27px;color:var(--white);font-weight:500;font-size:14px;line-height:17px}
.nav-btn{position:absolute;top:43px;height:34px;background:var(--brand-dark);color:var(--white);
  font-size:13px;font-weight:500;display:flex;align-items:center;justify-content:center;gap:6px}
.nav-user{left:761px;width:172px}
.nav-help{left:936px;width:92px}

.sidebar{position:absolute;left:171px;top:102px;width:218px;height:485px;background:var(--side-bg);box-shadow:0 0 4px rgba(0,0,0,.2)}
.menu{list-style:none}
.menu li{height:32px;display:flex;align-items:center;padding-left:18px;gap:14px;font-size:13px;color:var(--muted);
  border-bottom:1px solid #c9c9c9;background:linear-gradient(#f4f4f4,#e8e8e8)}
.menu li.active{height:38px;background:var(--brand);color:var(--white);font-weight:500;border:0;position:relative}
.menu li.active::after{content:"";position:absolute;right:-7px;top:14px;border:6px solid transparent;border-left:0;border-right-color:var(--white);right:-9px}
.menu svg{width:18px;height:18px;fill:var(--brand)}
.menu li.active svg{fill:var(--white)}
.quote{padding:28px 12px 0}
.quote h2{display:flex;align-items:center;gap:8px;color:var(--brand);font-size:15px;font-weight:700;margin-left:5px;margin-bottom:8px}
.field{height:29px;margin-bottom:4px;border:1px solid #c4c4c4;border-radius:3px;background:linear-gradient(#fff,#ececec);
  display:flex;align-items:center;justify-content:space-between;padding:0 9px 0 11px;font-size:12px;color:#888}
.field.message{height:67px;align-items:flex-start;padding-top:8px}
.field svg{fill:#8a8a8a}
.send{margin:4px 0 0 auto;width:75px;height:27px;background:var(--brand);color:var(--white);border-radius:3px;
  font-size:10px;font-weight:700;display:flex;align-items:center;justify-content:center;gap:5px}

.panel{position:absolute;left:398px;top:102px;width:631px;height:485px;background:var(--white);box-shadow:0 0 5px rgba(0,0,0,.18)}
.panel-title{position:absolute;left:19px;top:19px;font-size:19px;font-weight:400;color:#6a6a6a;letter-spacing:-.2px}
.panel-title strong{color:var(--brand);font-weight:700}
.panel-rule{position:absolute;left:19px;right:21px;top:43px;height:1px;background:var(--rule)}
.stats{position:absolute;left:19px;top:43px;width:591px;display:grid;grid-template-columns:290px 290px;column-gap:11px}
.stat{position:relative;height:146px;padding:28px 0 0 5px;border-bottom:1px solid var(--rule)}
.stat:nth-last-child(-n+2){border-bottom:0}
.stat h3{font-size:12px;font-weight:500;color:var(--muted);line-height:14px;width:180px}
.stat h3.lead{color:var(--brand)}
.stat p{font-size:10px;line-height:12px;color:#444;width:160px;margin-top:1px}
.stat .gap{margin-top:15px}
.view{position:absolute;left:5px;top:104px;font-size:10px;font-weight:700;color:var(--brand);letter-spacing:.2px}
.ring{position:absolute;right:4px;top:28px;width:98px;height:98px}
.ring-label{position:absolute;right:4px;top:28px;width:98px;height:98px;display:flex;flex-direction:column;align-items:center;justify-content:center;
  color:var(--brand);font-size:19px;font-weight:700;line-height:19px}
.ring-label small{font-size:10px;line-height:11px}

.footer{position:absolute;left:0;top:614px;width:1200px;height:44px;background:var(--footer)}
.social{position:absolute;top:10px;width:25px;height:25px;border-radius:50%;background:#555}
.copy{position:absolute;right:176px;top:17px;font-size:10px;color:#9a9a9a}
</style>
</head>
<body>
<div class="backdrop" role="img" aria-label="Soft grey background photo of floating bank notes and percentage figures"></div>

<header class="topbar">
  <div class="brand"><span class="brand-dot"></span><span class="brand-name">Vomil Brixton Solutions</span></div>
  <span class="brand-divider"></span>
  <div class="app-title">Call out and<br>support tracker</div>
  <div class="nav-btn nav-user">
    <svg width="16" height="16" viewBox="0 0 16 16" fill="#fff"><circle cx="8" cy="5" r="4"/><path d="M0 16c0-5 3-6.5 8-6.5s8 1.5 8 6.5z"/></svg>
    Martin Ellery
    <svg width="10" height="6" viewBox="0 0 10 6" fill="#fff"><path d="M0 0h10L5 6z"/></svg>
  </div>
  <div class="nav-btn nav-help">
    <svg width="15" height="15" viewBox="0 0 16 16"><circle cx="8" cy="8" r="7" fill="none" stroke="#fff" stroke-width="1.6"/><rect x="7.1" y="6.5" width="1.8" height="5.5" fill="#fff"/><circle cx="8" cy="4.5" r="1.1" fill="#fff"/></svg>
    Help
  </div>
</header>

<aside class="sidebar">
  <ul class="menu">
    <li class="active"><svg viewBox="0 0 18 18"><path d="M9 2 1 9h2.5v7h4v-5h3v5h4V9H17z"/></svg>Home</li>
    <li><svg viewBox="0 0 18 18"><circle cx="9" cy="9" r="6.5" fill="none" stroke="#1f4a9e" stroke-width="3"/><circle cx="9" cy="9" r="2.5"/></svg>Jobs</li>
    <li><svg viewBox="0 0 18 18"><circle cx="6" cy="6" r="3"/><circle cx="12" cy="6" r="3"/><path d="M0 15c0-4 2-5 6-5s6 1 6 5zM8 15c0-4 2-5 4-5s6 1 6 5z"/></svg>Customers</li>
    <li><svg viewBox="0 0 18 18"><rect x="1" y="9" width="12" height="7"/><circle cx="12" cy="6" r="4"/></svg>Inventory</li>
    <li><svg viewBox="0 0 18 18"><rect x="1" y="2" width="16" height="11" fill="none" stroke="#1f4a9e" stroke-width="1.6"/><rect x="5" y="8" width="2" height="3"/><rect x="8" y="6" width="2" height="5"/><rect x="11" y="4" width="2" height="7"/><path d="M8 13h2v4H8z"/></svg>Reports</li>
    <li><svg viewBox="0 0 18 18"><path d="M1 4h6l2 2h8v10H1z"/></svg>Files</li>
    <li><svg viewBox="0 0 18 18"><rect x="3" y="1" width="12" height="16" fill="none" stroke="#1f4a9e" stroke-width="1.6"/><rect x="6" y="5" width="3" height="5"/><rect x="10" y="9" width="3" height="1.5"/><rect x="6" y="12" width="7" height="1.5"/></svg>Quotes</li>
  </ul>
  <form class="quote">
    <h2><svg width="22" height="20" viewBox="0 0 22 20"><path d="M1 8 11 1l10 7v11H1z" fill="none" stroke="#1f4a9e" stroke-width="1.6"/><path d="M1 8l10 7 10-7" fill="none" stroke="#1f4a9e" stroke-width="1.6"/></svg>REQUEST A QUOTE</h2>
    <div class="field">Name<svg width="12" height="13" viewBox="0 0 12 13"><circle cx="6" cy="3.5" r="3.3"/><path d="M0 13c0-4 2-5.5 6-5.5s6 1.5 6 5.5z"/></svg></div>
    <div class="field">Email<svg width="16" height="12" viewBox="0 0 16 12"><path d="M1 1h14v10H1zM1 1l7 6 7-6" fill="none" stroke="#8a8a8a" stroke-width="1.4"/></svg></div>
    <div class="field message">Message<svg width="14" height="11" viewBox="0 0 14 11"><rect y="0" width="14" height="1.8"/><rect y="3" width="14" height="1.8"/><rect y="6" width="14" height="1.8"/><rect y="9" width="14" height="1.8"/></svg></div>
    <div class="send">SEND<svg width="11" height="11" viewBox="0 0 12 12"><path d="M5 7l2-2M4 5 2 7a2 2 0 0 0 3 3l2-2M8 7l2-2a2 2 0 0 0-3-3L5 4" fill="none" stroke="#fff" stroke-width="1.5"/></svg></div>
  </form>
</aside>

<main class="panel">
  <h1 class="panel-title"><strong>DASHBOARD</strong> STATISTICS OVERVIEW</h1>
  <div class="panel-rule"></div>
  <section class="stats">
    <article class="stat">
      <h3 class="lead">Number of support tickets logged per month</h3>
      <p>Lorem ipsum dolor sit amet, consectetuer adipiscing elit, sed diam nonummy...</p>
      <span class="view">VIEW INFO</span>
      <svg class="ring" viewBox="0 0 100 100"><circle cx="50" cy="50" r="46" fill="none" stroke="var(--ring-grey)" stroke-width="7"/><circle cx="50" cy="50" r="46" fill="none" stroke="var(--brand)" stroke-width="7" pathLength="100" stroke-dasharray="70 100" transform="rotate(-120 50 50) scale(1 -1) translate(0 -100)"/></svg>
      <div class="ring-label">70%</div>
    </article>
    <article class="stat">
      <h3>Number of currently open support tickets</h3>
      <p>Ut wisi enim ad minim veniam, quis nostrud exerci tation ullamcorper suscipit lobortis nis....</p>
      <span class="view">VIEW INFO</span>
      <svg class="ring" viewBox="0 0 100 100"><circle cx="50" cy="50" r="46" fill="none" stroke="var(--ring-grey)" stroke-width="7"/><circle cx="50" cy="50" r="46" fill="none" stroke="var(--brand)" stroke-width="7" pathLength="100" stroke-dasharray="84 100" transform="rotate(-90 50 50) scale(1 -1) translate(0 -100)"/></svg>
      <div class="ring-label">84%</div>
    </article>
    <article class="stat">
      <h3>Number of Quote Requests awaiting a response</h3>
      <p>Duis autem vel eum iriure dolor in hendrerit in vulputate velit esse molestie consequat,...</p>
      <span class="view">VIEW INFO</span>
      <svg class="ring" viewBox="0 0 100 100"><circle cx="50" cy="50" r="46" fill="none" stroke="var(--ring-grey)" stroke-width="7"/><circle cx="50" cy="50" r="46" fill="none" stroke="var(--brand)" stroke-width="7" pathLength="100" stroke-dasharray="20 100" transform="rotate(-90 50 50) scale(1 -1) translate(0 -100)"/></svg>
      <div class="ring-label">20%</div>
    </article>
    <article class="stat">
      <h3>Number of Files and file repository</h3>
      <p>Lorem ipsum dolor sit amet, consectetuer adipiscing elit, sed diam nonummy...</p>
      <span class="view">VIEW INFO</span>
      <svg class="ring" viewBox="0 0 100 100"><circle cx="50" cy="50" r="46" fill="none" stroke="var(--ring-grey)" stroke-width="7"/><circle cx="50" cy="50" r="46" fill="none" stroke="var(--brand)" stroke-width="7" pathLength="100" stroke-dasharray="50 100" transform="rotate(-90 50 50) scale(1 -1) translate(0 -100)"/></svg>
      <div class="ring-label">500</div>
    </article>
    <article class="stat">
      <h3>Number of Reports</h3>
      <p class="gap">Lorem ipsum dolor sit amet, consectetuer adipiscing elit, sed diam nonummy...</p>
      <span class="view">VIEW INFO</span>
      <svg class="ring" viewBox="0 0 100 100"><circle cx="50" cy="50" r="46" fill="none" stroke="var(--ring-grey)" stroke-width="7"/><circle cx="50" cy="50" r="46" fill="none" stroke="var(--brand)" stroke-width="7" pathLength="100" stroke-dasharray="50 100" transform="rotate(-90 50 50) scale(1 -1) translate(0 -100)"/></svg>
      <div class="ring-label">503<small>Reports</small></div>
    </article>
    <article class="stat">
      <h3>Number of Customers</h3>
      <p class="gap">Ut wisi enim ad minim veniam, quis nostrud exerci tation ullamcorper suscipit lobortis nis....</p>
      <span class="view">VIEW INFO</span>
      <svg class="ring" viewBox="0 0 100 100"><circle cx="50" cy="50" r="46" fill="none" stroke="var(--ring-grey)" stroke-width="7"/><circle cx="50" cy="50" r="46" fill="none" stroke="var(--brand)" stroke-width="7" pathLength="100" stroke-dasharray="62 100" transform="rotate(-90 50 50) scale(1 -1) translate(0 -100)"/></svg>
      <div class="ring-label">702<small>Customers</small></div>
    </article>
  </section>
</main>

<footer class="footer">
  <span class="social" style="left:176px"></span>
  <span class="social" style="left:213px"></span>
  <span class="copy">© Vomil Brixton Solutions. 2014</span>
</footer>
</body>
</html>
```